Präsentationsvorlagen für Unternehmensberatung im Finanzbereich
Zielgruppe
Unternehmensberatung für den Finanzbereich, Compliance Beratung/Implementierung regulatorischer Projekte, Bereitstellung von Management Resourcen, Trainings/Coaching/Seminare. Zielgruppe: Banken, Fonds und Investmentgesellschaften
Aufgabenstellung
hochwertiges design, clean, keine standard bilder von Bergen, Tastaturen oder Menschen, die sich unterhalten. eher Architektur Bilder, Bilder sollen Bezug zum Inhalt haben, Verlässlichkeit, Professionalität, Kundenfokus ausstrahlen. 4 Services sollen präsentiert werden, ggf mit Bildlogo in unterschiedlichen Farben verbinden.

```html
<!DOCTYPE html>
<html lang="de">
<head>
<meta charset="UTF-8">
<title>Service I – Beispiel Muster</title>
<link rel="stylesheet" href="https://fonts.googleapis.com/css2?family=Playfair+Display:wght@400&family=Roboto+Mono:wght@300&family=Roboto:wght@300&display=swap">
<style>
  :root {
    --paper: #ffffff;
    --ink: #111111;
    --panel: #e9e9e9;
    --panel-dark: #8c8c8c;
    --numeral: #dcdcdc;
    --rule: #1a1a1a;
  }
  html, body {
    margin: 0;
    padding: 0;
    overflow: hidden;
    background: var(--paper);
  }
  .slide {
    position: relative;
    width: 1200px;
    height: 675px;
    overflow: hidden;
    background: var(--paper);
  }
  .hero-image {
    position: absolute;
    left: 382px;
    top: 127px;
    right: 0;
    bottom: 0;
    background:
      linear-gradient(150deg, var(--panel) 0%, var(--panel) 38%, #cfcfcf 55%, #a9a9a9 78%, var(--panel-dark) 100%);
  }
  .section-number {
    position: absolute;
    left: 432px;
    top: 120px;
    font-family: "Roboto", sans-serif;
    font-weight: 300;
    font-size: 320px;
    line-height: 1;
    letter-spacing: -6px;
    color: var(--numeral);
    opacity: 0.85;
    margin: 0;
  }
  .title {
    position: absolute;
    left: 106px;
    top: 70px;
    margin: 0;
    font-family: "Playfair Display", serif;
    font-weight: 400;
    font-size: 80px;
    line-height: 72px;
    letter-spacing: -1px;
    color: var(--ink);
  }
  .service-text {
    position: absolute;
    left: 67px;
    top: 345px;
    margin: 0;
    font-family: "Roboto Mono", monospace;
    font-weight: 300;
    font-size: 20px;
    line-height: 32px;
    color: var(--ink);
  }
  .footer-label {
    position: absolute;
    left: 67px;
    top: 601px;
    margin: 0;
    font-family: "Roboto Mono", monospace;
    font-weight: 300;
    font-size: 14px;
    line-height: 20px;
    color: var(--ink);
  }
  .footer-rule {
    position: absolute;
    left: 331px;
    right: 0;
    top: 611px;
    height: 1px;
    background: var(--rule);
  }
</style>
</head>
<body>
  <main class="slide">
    <div class="hero-image" role="img" aria-label="Schwarz-weiße Architekturaufnahme: Ecke eines modernen Bürogebäudes mit gebogener Fassade und Fensterreihen vor hellem Himmel"></div>
    <p class="section-number">02</p>
    <h1 class="title">Service I<br>Beispiel Muster</h1>
    <p class="service-text">Service I Muster<br>xxxxx xxx x x xxxx<br>xxxx xxxxx xxxxxxx<br>MUSTER xxxx</p>
    <p class="footer-label">Compliance Beratung</p>
    <div class="footer-rule"></div>
  </main>
</body>
</html>
```